GetShelf screenshots

We need an GetShelf screenshot design for our app. The design should be for the all Nuvadexes and Korvis. Please see attached for sample (Nuvadex & Korvi) and images. Use the website www.plomvex.com for color guidance.

```html
<!DOCTYPE html>
<html lang="en">
<head>
<meta charset="utf-8">
<title>Track monthly trends</title>
<link rel="stylesheet" href="https://fonts.googleapis.com/css2?family=Inter:wght@700;800&family=Open+Sans:wght@400;600;700&display=swap">
<style>
  :root {
    --page-bg: #f8fafc;
    --wave-blue: #2f7ec1;
    --navy: #322d4f;
    --headline: #2f2b4f;
    --accent-line: #3a85d6;
    --bezel: #1b1b1f;
    --bezel-edge: #8a8a8e;
    --screen-bg: #ffffff;
    --teal: #3ddbb4;
    --tab-active: #2fbf7a;
    --bar-positive: #3d6aa3;
    --bar-negative: #5a1616;
    --marker: #ff2a2a;
    --axis: #cfcfcf;
    --ink: #1e1e1e;
  }
  html, body { margin: 0; padding: 0; }
  body { width: 743px; height: 1200px; overflow: hidden; background: var(--page-bg); }
  .canvas { position: relative; width: 743px; height: 1200px; overflow: hidden; }
  .backdrop { position: absolute; inset: 0; }
  .headline {
    position: absolute; top: 138px; left: 0; width: 743px; margin: 0;
    text-align: center; font-family: "Inter", sans-serif; font-weight: 800;
    font-size: 47px; letter-spacing: -1.4px; color: var(--headline);
  }
  .device {
    position: absolute; left: 160px; top: 292px; width: 403px; height: 814px;
    border-radius: 60px; background: var(--bezel);
    box-shadow: 0 0 0 3px var(--bezel-edge);
  }
  .screen {
    position: absolute; left: 184px; top: 314px; width: 355px; height: 771px;
    border-radius: 40px; overflow: hidden; background: var(--screen-bg);
    font-family: "Open Sans", sans-serif;
  }
  .topbar {
    position: absolute; left: 0; top: 0; width: 100%; height: 75px; background: var(--navy); color: #fff;
  }
  .notch {
    position: absolute; left: 80px; top: 0; width: 195px; height: 28px;
    background: var(--bezel); border-radius: 0 0 20px 20px;
  }
  .status-time { position: absolute; left: 27px; top: 10px; font-size: 13px; font-weight: 600; }
  .status-icons { position: absolute; right: 18px; top: 13px; }
  .screen-title {
    position: absolute; left: 0; top: 47px; width: 100%; text-align: center;
    font-size: 14px; font-weight: 400; letter-spacing: 0.2px;
  }
  .back { position: absolute; left: 10px; top: 48px; }
  .filter-label {
    position: absolute; left: 14px; top: 97px; font-size: 18px; font-weight: 600; color: var(--teal);
  }
  .chart { position: absolute; left: 0; top: 0; }
  .chart text { font-family: "Open Sans", sans-serif; font-weight: 700; font-size: 12.5px; fill: var(--ink); }
  .tabbar {
    position: absolute; left: 0; bottom: 0; width: 100%; height: 77px; background: var(--navy);
  }
  .tab { position: absolute; top: 15px; font-size: 14px; font-weight: 700; transform: translateX(-50%); }
  .tab-about { left: 88px; color: #fff; }
  .tab-trend { left: 267px; color: var(--tab-active); }
  .home-indicator {
    position: absolute; left: 114px; bottom: 6px; width: 127px; height: 4px; border-radius: 2px; background: #fff;
  }
</style>
</head>
<body>
<div class="canvas">
  <svg class="backdrop" width="743" height="1200" viewBox="0 0 743 1200" aria-hidden="true">
    <path d="M0 413 C 260 490, 420 700, 667 726 C 700 727, 720 723, 743 720 V1200 H0 Z" fill="var(--wave-blue)"/>
    <path d="M0 562 C 250 690, 420 880, 743 895 V1200 H0 Z" fill="var(--navy)"/>
    <line x1="616" y1="420" x2="667" y2="420" stroke="var(--navy)" stroke-width="2"/>
    <circle cx="-25" cy="716" r="64" fill="none" stroke="var(--accent-line)" stroke-width="1.6"/>
    <line x1="56" y1="934" x2="56" y2="1001" stroke="var(--accent-line)" stroke-width="1.6"/>
    <line x1="22" y1="967" x2="90" y2="967" stroke="var(--accent-line)" stroke-width="1.6"/>
  </svg>

  <h1 class="headline">Track monthly trends</h1>

  <div class="device"></div>
  <div class="screen">
    <div class="topbar">
      <div class="notch"></div>
      <span class="status-time">2:28</span>
      <svg class="status-icons" width="62" height="12" viewBox="0 0 62 12" aria-hidden="true">
        <rect x="0" y="7" width="2.5" height="4" fill="#fff"/>
        <rect x="4" y="5" width="2.5" height="6" fill="#fff"/>
        <rect x="8" y="3" width="2.5" height="8" fill="#fff"/>
        <rect x="12" y="1" width="2.5" height="10" fill="#fff" opacity="0.4"/>
        <path d="M20 5 a9 9 0 0 1 12 0 M22.5 7.5 a5 5 0 0 1 7 0" stroke="#fff" stroke-width="1.6" fill="none"/>
        <circle cx="26" cy="10" r="1.3" fill="#fff"/>
        <rect x="39" y="1.5" width="20" height="9" rx="2.5" fill="none" stroke="#fff" stroke-width="1"/>
        <rect x="41" y="3.5" width="13" height="5" rx="1" fill="#fff"/>
        <rect x="60" y="4.5" width="1.5" height="3" fill="#fff"/>
      </svg>
      <svg class="back" width="14" height="20" viewBox="0 0 14 20" aria-hidden="true">
        <path d="M11 2 L3 10 L11 18" stroke="#fff" stroke-width="2.2" fill="none" stroke-linecap="round" stroke-linejoin="round"/>
      </svg>
      <div class="screen-title">GOVERNMENTHOLDINGS</div>
    </div>

    <div class="filter-label">ALL</div>

    <svg class="chart" width="355" height="700" viewBox="0 0 355 700" aria-label="Monthly holdings bar chart">
      <line x1="52" y1="140" x2="52" y2="619" stroke="var(--axis)" stroke-width="1"/>
      <line x1="52" y1="619" x2="330" y2="619" stroke="var(--axis)" stroke-width="1"/>
      <g text-anchor="end">
        <text x="46" y="164">Oct</text>
        <text x="46" y="204">Nov</text>
        <text x="46" y="244">Dec</text>
        <text x="46" y="284">Jan</text>
        <text x="46" y="324">Feb</text>
        <text x="46" y="364">Mar</text>
        <text x="46" y="404">Apr</text>
        <text x="46" y="444">May</text>
        <text x="46" y="484">Jun</text>
        <text x="46" y="524">Jul</text>
        <text x="46" y="564">Aug</text>
        <text x="46" y="604">Sep</text>
      </g>
      <rect x="52" y="149" width="236" height="23" fill="var(--bar-positive)"/>
      <rect x="263" y="150" width="2" height="20" fill="var(--marker)"/>
      <text x="293" y="165">116.8B</text>
      <rect x="52" y="189" width="114" height="22" fill="var(--bar-negative)"/>
      <rect x="160" y="190" width="2" height="20" fill="var(--marker)"/>
      <text x="170" y="205">-56.32B</text>
      <g text-anchor="middle">
        <text x="55" y="637">0</text>
        <text x="127" y="637">29.20B</text>
        <text x="183" y="637">58.39B</text>
        <text x="239" y="637">87.59B</text>
        <text x="295" y="637">116.8B</text>
      </g>
    </svg>

    <div class="tabbar">
      <span class="tab tab-about">About</span>
      <span class="tab tab-trend">Trend</span>
      <div class="home-indicator"></div>
    </div>
  </div>
</div>
</body>
</html>
```